Stationery Design Project

I need a stationary design for our company. we are based in Houston, TX and we are called Vell Marot Lending. And we are wanting to brand our FundMendWise program, which includes our tax preparation and restoration, credit repair service. Although our business offers other programs, we are interested in mainly focusing on The FundMendWise program. We are looking for way to brand our ourselves and I believe that a great stationery design will help in achieving this goal. Our logo design is blue and light blue. the slogan is orange.

Industry/Entity Type

Business

Requirements
Must have
• Address: 30871 Birchhollow Ln. K-22
Houston, TX 77419
Tel. 832-516-3928
Fax 713-264-9187
www.vellmarotlending-example.com
info@vellmarotlending-example.com
Our Slogan: Confidence, Renewed!

```html
<!DOCTYPE html>
<html lang="en">
<head>
<meta charset="utf-8">
<title>FundMendWise Stationery – Business Cards</title>
<link rel="stylesheet" href="https://fonts.googleapis.com/css2?family=Jost:wght@400;500&family=Cinzel:wght@600&family=Libre+Baskerville&display=swap">
<style>
  :root {
    --backdrop: #e8e3dc;
    --card-white: #ffffff;
    --navy: #123c64;
    --brand-blue: #1d5f98;
    --light-blue: #a9cbe6;
    --orange: #f0921e;
    --ink: #333333;
    --label: #1a1a1a;
  }
  * { box-sizing: border-box; margin: 0; padding: 0; }
  html, body { width: 1200px; height: 800px; overflow: hidden; }
  body { background: var(--backdrop); position: relative; font-family: "Jost", sans-serif; }

  .view-label {
    position: absolute; width: 508px; text-align: center;
    font-family: "Jost", sans-serif; font-size: 21px; color: var(--label);
  }

  .card {
    position: absolute; width: 508px; height: 290px;
    border-radius: 20px; overflow: hidden;
    box-shadow: 0 4px 10px rgba(0,0,0,0.25);
  }
  .card--light { background: var(--card-white); }
  .card--dark { background: var(--navy); }
  .card__curves { position: absolute; inset: 0; }

  .brand-name {
    position: absolute; left: 0; right: 0; text-align: center; white-space: nowrap;
  }
  .front__name {
    top: 118px; font-family: "Jost", sans-serif; font-weight: 500;
    font-size: 50px; color: var(--brand-blue); letter-spacing: 0.5px;
  }
  .front__contact {
    position: absolute; left: 0; right: 0; top: 202px; text-align: center;
    font-size: 14px; line-height: 21px; color: var(--ink); white-space: nowrap;
  }

  .slogan {
    position: absolute; left: 0; right: 0; text-align: center;
    font-family: "Cinzel", serif; font-weight: 600; font-size: 20px;
    color: var(--orange); letter-spacing: 0.4px; white-space: nowrap;
  }
  .website {
    position: absolute; left: 0; right: 0; text-align: center; white-space: nowrap;
    font-family: "Jost", sans-serif; font-size: 20px; letter-spacing: 1.4px;
  }
  .card--light .website { color: var(--ink); }
  .card--dark .website { color: #ffffff; }

  .emblem-box {
    position: absolute; left: 168px; width: 172px; height: 170px;
    display: flex; align-items: center; justify-content: center; text-align: center;
  }
  .emblem-box--filled {
    background: var(--navy); outline: 1px solid var(--brand-blue); outline-offset: 3px;
  }
  .emblem-box--framed { border: 4px solid var(--light-blue); }
  .emblem-box__name {
    font-family: "Libre Baskerville", serif; font-size: 15px; line-height: 22px; color: #ffffff;
  }

  .mark-square {
    position: absolute; left: 222px; top: 80px; width: 64px; height: 64px;
    border: 3px solid var(--light-blue);
  }
  .back2__name {
    top: 202px; font-family: "Libre Baskerville", serif; font-size: 20px; color: #ffffff;
  }
</style>
</head>
<body>

  <div class="view-label" style="left:72px; top:50px;">Front</div>
  <div class="view-label" style="left:621px; top:50px;">Back - 1</div>
  <div class="view-label" style="left:75px; top:410px;">Back - 2</div>
  <div class="view-label" style="left:621px; top:410px;">Back - 3</div>

  <!-- Front -->
  <section class="card card--light" style="left:72px; top:90px;">
    <svg class="card__curves" viewBox="0 0 508 290" aria-hidden="true">
      <path d="M448 0 Q502 18 508 78 L508 0 Z" fill="var(--brand-blue)"/>
      <path d="M436 0 Q500 22 508 96" fill="none" stroke="var(--orange)" stroke-width="2.5"/>
      <path d="M0 208 Q8 276 72 290 L0 290 Z" fill="var(--brand-blue)"/>
      <path d="M0 188 Q12 282 92 290" fill="none" stroke="var(--orange)" stroke-width="2.5"/>
    </svg>
    <div class="brand-name front__name">FundMendWise</div>
    <div class="front__contact">
      <p>p : 832-516-3928 | f : 713-264-9187</p>
      <p>e : info@vellmarotlending-example.com | w : www.vellmarotlending-example.com</p>
      <p>30871 Birchhollow Ln. K-22, Houston, TX 77419</p>
    </div>
  </section>

  <!-- Back 1 -->
  <section class="card card--light" style="left:621px; top:90px;">
    <p class="slogan" style="top:22px;">Confidence, Renewed!</p>
    <div class="emblem-box emblem-box--filled" style="top:62px;">
      <span class="emblem-box__name">Vell Marot<br>Lending</span>
    </div>
    <p class="website" style="top:243px;">www.vellmarotlending-example.com</p>
  </section>

  <!-- Back 2 -->
  <section class="card card--dark" style="left:75px; top:450px;">
    <p class="slogan" style="top:20px;">Confidence, Renewed!</p>
    <div class="mark-square" aria-hidden="true"></div>
    <div class="brand-name back2__name">Vell Marot Lending</div>
    <p class="website" style="top:248px;">www.vellmarotlending-example.com</p>
  </section>

  <!-- Back 3 -->
  <section class="card card--dark" style="left:621px; top:450px;">
    <p class="slogan" style="top:20px;">Confidence, Renewed!</p>
    <div class="emblem-box emblem-box--framed" style="top:55px;">
      <span class="emblem-box__name">Vell Marot<br>Lending</span>
    </div>
    <p class="website" style="top:248px;">www.vellmarotlending-example.com</p>
  </section>

</body>
</html>
```